Business Card Design/Logo

I require a design/logo for my own Company, Morvix. The Jewellery I make is totally hand crafted. I own a hand Mining Claim out in the gemfields of Queensland and dig up my own stones. I also fossick for Gold Locally so all my Jewellery products are hand dug/cut/created. Quality stones are hand cut by my partner (Faceted) and other stones (Seconds) are either skin polished or recessed into pieces of Solid 925 Silver or Solid 9ct and 18 ct Gold. I make Sets (Collections) or just one-of designs. All the stones come in different colours and I am now starting to use different colour Golds. The final design should radiate professionalism, quality and uniqueness.

Target Market(s)

Many designs will cost a minimum of AU Dollars $2,000

Industry/Entity Type

Business

Contact Information for Business Card

Morvix Creations
Distinct Bench Wrought Native Adornments
0400327986
P.O. Box 418 Ambercrest 4719 Qld
morvixgarnets@mailbrook.net

```html
<!DOCTYPE html>
<html lang="en">
<head>
<meta charset="utf-8">
<title>Morvix Creations – Business Card</title>
<link rel="stylesheet" href="https://fonts.googleapis.com/css2?family=Oswald:wght@300&family=Arimo:wght@400&display=swap">
<style>
  :root {
    --ink-white: #ffffff;
    --card-black: #0b0b0b;
    --leather-dark: #1c1c1c;
    --leather-mid: #3a3a3a;
    --stone-glow: #e9e9e9;
    --rule: #d8d8d8;
  }
  html, body {
    margin: 0;
    padding: 0;
    width: 1200px;
    height: 693px;
    overflow: hidden;
    background: var(--card-black);
  }
  .card {
    position: relative;
    width: 1200px;
    height: 693px;
    overflow: hidden;
    background: var(--card-black);
  }
  .gem-photo {
    position: absolute;
    inset: 0;
    background:
      radial-gradient(ellipse 420px 150px at 610px 270px, rgba(233,233,233,0.55), rgba(233,233,233,0) 100%),
      radial-gradient(ellipse 160px 110px at 170px 250px, rgba(233,233,233,0.45), rgba(233,233,233,0) 100%),
      radial-gradient(ellipse 150px 110px at 1050px 250px, rgba(233,233,233,0.4), rgba(233,233,233,0) 100%),
      radial-gradient(ellipse 900px 380px at 580px 230px, var(--leather-mid), var(--leather-dark) 60%, var(--card-black) 100%);
  }
  .email {
    position: absolute;
    top: 30px;
    right: 40px;
    margin: 0;
    font-family: "Arimo", Arial, sans-serif;
    font-size: 22px;
    color: var(--ink-white);
  }
  .divider {
    position: absolute;
    left: 70px;
    top: 460px;
    width: 1062px;
    height: 2px;
    background: var(--rule);
  }
  .brand-name {
    position: absolute;
    left: 0;
    top: 480px;
    width: 1200px;
    height: 120px;
  }
  .brand-name text {
    font-family: "Oswald", "Arial Narrow", sans-serif;
    font-weight: 300;
    font-size: 118px;
    fill: var(--ink-white);
  }
  .tagline {
    position: absolute;
    left: 0;
    width: 1200px;
    top: 622px;
    margin: 0;
    text-align: center;
    font-family: "Arimo", Arial, sans-serif;
    font-size: 22px;
    color: var(--ink-white);
    white-space: nowrap;
  }
</style>
</head>
<body>
  <main class="card">
    <div class="gem-photo" role="img" aria-label="Photograph of sparkling clear faceted gemstones scattered on dark textured leather"></div>
    <p class="email">morvixgarnets@mailbrook.net</p>
    <div class="divider"></div>
    <svg class="brand-name" viewBox="0 0 1200 120" aria-label="Morvix Creations">
      <text x="72" y="106" textLength="1058" lengthAdjust="spacing">MORVIX CREATIONS</text>
    </svg>
    <p class="tagline">Distinct Bench Wrought Native Adornments 0400327986 P.O. Box 418 Ambercrest 4719 Qld</p>
  </main>
</body>
</html>
```